Webinar email campaign graphic/template

We need a static email campaign graphic that can be customized for a variety of communications - webinar announcement, whitepaper distribution, etc. Need ability to edit the files for text content. Attached are current examples/format. Please refer to website for design theme/ideas. www.k7cargoledger.com

Target Market(s)

Transportation executives

Industry/Entity Type

All

Requirements
Must have
• Ability to customize text for headers/content
Should not have
• Inability to edit text

```html
<!DOCTYPE html>
<html lang="en">
<head>
<meta charset="utf-8">
<title>Best Practices for Procuring a Freight Payment Solution</title>
<link rel="stylesheet" href="https://fonts.googleapis.com/css2?family=Noto+Sans:ital,wght@1,900&family=Roboto:ital,wght@0,700;0,900;1,900&family=Roboto+Condensed:ital,wght@1,400&display=swap">
<style>
  :root {
    --navy: #023c7e;
    --orange: #e86d14;
    --ink: #1b1b1b;
    --paper: #ffffff;
    --rule: #1c4580;
  }
  * { margin: 0; padding: 0; box-sizing: border-box; }
  html, body { width: 1200px; height: 900px; overflow: hidden; background: var(--paper); }
  .campaign { position: relative; width: 1200px; height: 900px; overflow: hidden; background: var(--paper); color: var(--ink); }

  .brand-name { position: absolute; left: 30px; top: 68px; font-family: "Roboto", sans-serif; font-weight: 700; font-size: 24px; line-height: 1; color: var(--navy); }

  .headline { position: absolute; left: 281px; top: 48px; font-family: "Roboto", sans-serif; font-style: italic; font-weight: 900; font-size: 78px; line-height: 1; color: var(--navy); letter-spacing: 0.5px; white-space: nowrap; }
  .subhead { position: absolute; left: 0; width: 1200px; top: 136px; text-align: center; font-family: "Noto Sans", sans-serif; font-style: italic; font-weight: 900; font-size: 50px; line-height: 1.1; color: var(--navy); letter-spacing: -0.3px; white-space: nowrap; }

  .hero { position: absolute; left: 0; top: 190px; width: 1200px; height: 225px; }

  .body-copy { position: absolute; left: 42px; width: 1140px; top: 436px; font-family: "Roboto Condensed", sans-serif; font-style: italic; font-size: 25.5px; line-height: 31.5px; letter-spacing: -0.35px; }
  .body-copy p + ul, .body-copy ul + p { margin-top: 31px; }
  .points { list-style: none; }
  .points li { position: relative; padding-left: 30px; }
  .points li::before { content: ""; position: absolute; left: 8px; top: 13px; width: 10px; height: 10px; border-radius: 50%; background: var(--ink); }

  .event-date { position: absolute; left: 42px; top: 796px; font-family: "Roboto", sans-serif; font-weight: 700; font-size: 30px; color: var(--navy); }
  .event-times { position: absolute; left: 42px; top: 838px; font-family: "Roboto Condensed", sans-serif; font-style: italic; font-size: 22.5px; color: var(--ink); }
  .event-times .sep { display: inline-block; width: 2px; height: 24px; background: var(--ink); vertical-align: -4px; margin: 0 6px 0 4px; }

  .rule { position: absolute; top: 868px; height: 2px; background: var(--rule); }
  .rule-left { left: 0; width: 410px; }
  .rule-right { left: 787px; width: 413px; }

  .register { position: absolute; left: 434px; top: 778px; width: 331px; height: 105px; border: 3px solid var(--orange); border-radius: 34px; padding: 4px; }
  .register span { display: flex; align-items: center; justify-content: center; width: 100%; height: 100%; background: var(--orange); border-radius: 29px; font-family: "Roboto", sans-serif; font-weight: 900; font-size: 47px; color: var(--paper); letter-spacing: 0.5px; }

  .site-url { position: absolute; left: 783px; top: 813px; font-family: "Roboto", sans-serif; font-weight: 700; font-size: 30px; color: var(--navy); }
</style>
</head>
<body>
<main class="campaign">
  <p class="brand-name">Cargo Ledger</p>

  <h1 class="headline">BEST PRACTICES</h1>
  <h2 class="subhead">for Procuring a Freight Payment Solution</h2>

  <svg class="hero" viewBox="0 0 1200 225" role="img" aria-label="Photo of semi trucks with headlights on driving along a highway at dusk">
    <defs>
      <linearGradient id="heroTone" x1="0" y1="0" x2="1" y2="0">
        <stop offset="0" stop-color="#b99a94"/>
        <stop offset="0.3" stop-color="#9c8f99"/>
        <stop offset="0.65" stop-color="#7e8290"/>
        <stop offset="1" stop-color="#8a93a0"/>
      </linearGradient>
      <linearGradient id="heroFade" x1="0" y1="0" x2="0" y2="1">
        <stop offset="0" stop-color="#ffffff" stop-opacity="1"/>
        <stop offset="0.3" stop-color="#ffffff" stop-opacity="0.35"/>
        <stop offset="0.6" stop-color="#ffffff" stop-opacity="0"/>
      </linearGradient>
    </defs>
    <polygon points="0,0 1200,0 1200,103 600,220 0,103" fill="url(#heroTone)"/>
    <polygon points="0,0 1200,0 1200,103 600,220 0,103" fill="url(#heroFade)"/>
    <polyline points="0,97 600,213 1200,97" fill="none" stroke="#ffffff" stroke-width="3"/>
    <polyline points="0,103 600,220 1200,103" fill="none" stroke="#5b6470" stroke-width="4"/>
  </svg>

  <section class="body-copy">
    <p>Lorem ipsum dolor sit amet, consectetuer adipiscing elit, sed diam nonummy nibh euismod tincidunt ut laoreet dolore magna aliquam erat volutpat. Ut wisi enim ad minim veniam, quis nostrud exerci tation</p>
    <ul class="points">
      <li>ullamcorper suscipit lobortis nisl ut aliquip</li>
      <li>hendrerit in vulputate velit esse molestie</li>
      <li>accumsan et iusto odio dignissim</li>
    </ul>
    <p>Lorem ipsum dolor sit amet, cons ectetuer adipiscing elit, sed diam nonummy nibh euismod tincidunt ut laoreet dolore magna aliquam erat volutpat. Ut wisi enim ad minim veniam, quis nostrud exerci tation ullamcorper suscipit lobortis nisl ut aliquip ex ea commodo consequat.</p>
  </section>

  <p class="event-date">Wednesday, July 26, 2021</p>
  <p class="event-times">11:30 Eastern<span class="sep"></span>10:30 Central<span class="sep"></span>8:30 Pacific</p>
  <div class="rule rule-left"></div>

  <div class="register"><span>REGISTER</span></div>

  <p class="site-url">www.k7cargoledger.com</p>
  <div class="rule rule-right"></div>
</main>
</body>
</html>
```